iPad Apps for Energy Industry w/ IT Consulting Business Needs a Brochure Design

We need a brochure and business card design for an IT development and consulting company based in Westlake Village, CA called "Copperfield Systems". We develop innovative iPad apps and provide IT consulting services for the Energy industry (specifically Oil and Gas companies).

For consulting services, we provide Business Intelligence solutions to implement Data Warehouse strategies. Our services include Business Intelligence, Data Warehouse, Application Integration and Support. An older consulting brochure we have used in the past under a different company name ("Norwell Data Advisory") is attached for additional background and content. We do not want to use the old design at all - its really just for reference only.

Our first product is called "Fieldpoint KRV" - includes iPad apps and web-based tools that support field production data gathering for Oil and Gas companies. It also includes a Decision Support Center (DSC) to help with route management of field operators using mapping technologies.

The final design should be an overview of the company, products and services with contact information.
Updates

We included some sample content for the areas of company overview, products and services for the brochure (added to attachment area - "Sample Content").  If there is too much content for your design, you do not need to use all of the sample.  We are flexible to re-write all areas to fit the design.

Please let us know if you need more information or have any additional questions about the brochure.

Contact information for the brochure below - 

4187 Halberton Ave. Suite 310
Westlake Village, CA. 91488
United States

+1-805-555-0173
info@copperfieldsystems-example.com
http://www.copperfieldsystems-example.com 

Please Note: Our website above is currently a placeholder, feel free to reference our previous site for additional details -  http://www.norwelldata-example.com

Target Market(s)

Oil and Gas company managers, males between 40 - 55 years old in corporate sector, college education, technical backgrounds

Industry/Entity Type

Industry

Requirements
Must have
• The bi-fold brochure must have 4 pages. It should measure 11" x 17" - folding to 8 1/2" x 11" for each page.
Nice to have
• We have a starter idea for the logo, but we would love to see other ideas. The starter logo ideas are attached but feel free to change it, thanks!

We would love the brochure to have different areas to highlight the company, products and services in an interesting way or layout. It should accommodate a good balance between photos/images and text but the brochure is an overview only of the products and services.

```html
<!DOCTYPE html>
<html lang="en">
<head>
<meta charset="utf-8">
<title>Copperfield Systems — Business Card</title>
<link rel="stylesheet" href="https://fonts.googleapis.com/css2?family=Nunito+Sans:ital,wght@0,400;0,600;0,700;1,400&display=swap">
<style>
  :root {
    --page-bg: #ffffff;
    --card-bg: #ffffff;
    --card-border: #1a1a1a;
    --brand-blue: #1f5aa8;
    --brand-sky: #3aa3dc;
    --brand-orange: #f08a24;
    --brand-yellow: #f7c948;
    --accent-red: #b3141b;
    --ink: #1a1a1a;
    --muted: #555b63;
    --dot-grey: #cfcfcf;
  }
  * { box-sizing: border-box; margin: 0; padding: 0; }
  html, body {
    width: 1200px;
    height: 415px;
    overflow: hidden;
    background: var(--page-bg);
    font-family: "Nunito Sans", Arial, sans-serif;
    color: var(--ink);
  }
  .canvas { position: relative; width: 1200px; height: 415px; }

  .card {
    position: absolute;
    top: 21px;
    height: 373px;
    background: var(--card-bg);
    border: 2px solid var(--card-border);
    overflow: hidden;
  }
  .card--front { left: 23px; width: 574px; }
  .card--back { left: 618px; width: 559px; }

  /* Front */
  .halftone-field {
    position: absolute;
    left: 0; top: 0;
    width: 400px; height: 373px;
    background: radial-gradient(ellipse at 0% 70%, var(--dot-grey) 0%, rgba(207,207,207,0.55) 40%, rgba(255,255,255,0) 75%);
  }
  .brand {
    position: absolute;
    top: 22px;
    left: 283px;
    display: flex;
    align-items: center;
    gap: 8px;
  }
  .brand__mark {
    width: 38px; height: 38px;
    border-radius: 50%;
    background: var(--brand-orange);
    flex: none;
  }
  .brand__name {
    font-weight: 600;
    font-size: 19px;
    line-height: 1.02;
    color: var(--brand-blue);
  }
  .brand__divider {
    width: 1px; height: 34px;
    background: var(--muted);
    margin: 0 2px;
  }
  .brand__tagline {
    font-size: 11px;
    line-height: 1.25;
    color: var(--muted);
  }
  .contact {
    position: absolute;
    right: 34px;
    top: 258px;
    text-align: right;
  }
  .contact__name {
    font-weight: 700;
    font-size: 19px;
    color: var(--accent-red);
    letter-spacing: 0.5px;
    line-height: 1.1;
  }
  .contact__position {
    font-style: italic;
    font-size: 14px;
    line-height: 1.3;
    margin-bottom: 8px;
  }
  .contact__line {
    font-size: 14px;
    line-height: 1.4;
  }

  /* Back */
  .emblem-field {
    position: absolute;
    left: 0; top: 0;
    width: 520px; height: 373px;
    background:
      linear-gradient(170deg, rgba(255,255,255,0) 60%, rgba(240,138,36,0.35) 75%, rgba(247,201,72,0.25) 85%, rgba(255,255,255,0) 95%),
      linear-gradient(105deg, rgba(31,90,168,0.55) 0%, rgba(58,163,220,0.35) 45%, rgba(255,255,255,0) 80%);
  }
  .back-web {
    position: absolute;
    left: 0; right: 0;
    top: 176px;
    text-align: center;
    font-weight: 600;
    font-size: 13px;
  }
  .back-address {
    position: absolute;
    left: 0; right: 0;
    top: 326px;
    text-align: center;
    font-weight: 600;
    font-size: 13.5px;
  }
</style>
</head>
<body>
  <main class="canvas">
    <section class="card card--front" aria-label="Business card front">
      <div class="halftone-field" role="img" aria-label="Soft grey halftone dot pattern fading toward the right"></div>
      <div class="brand">
        <span class="brand__mark" aria-hidden="true"></span>
        <span class="brand__name">Copperfield<br>Systems</span>
        <span class="brand__divider" aria-hidden="true"></span>
        <span class="brand__tagline">Creative Solutions<br>For Oil And Gas</span>
      </div>
      <div class="contact">
        <p class="contact__name">NAME</p>
        <p class="contact__position">Position</p>
        <p class="contact__line">Mobile: xxxx xxxx</p>
        <p class="contact__line">Email: info@copperfieldsystems-example.com</p>
      </div>
    </section>

    <section class="card card--back" aria-label="Business card back">
      <div class="emblem-field" role="img" aria-label="Large brand emblem area in blue and orange tones"></div>
      <p class="back-web">www.norwelldata-example.com</p>
      <p class="back-address">4187 Halberton Ave. Suite 310, Westlake Village, CA. 91488, United States</p>
    </section>
  </main>
</body>
</html>
```